Birch Flooring Supply

Basic one-sided business card design using the attached logo. Vintage americana theme. Font is modified Arial Nova Cond, but anything that coordinates can be used

```html
<!DOCTYPE html>
<html lang="en">
<head>
<meta charset="utf-8">
<title>Birch Flooring Supply – Business Card</title>
<link href="https://fonts.googleapis.com/css2?family=Arimo:wght@400;700&display=swap" rel="stylesheet">
<style>
  :root {
    --backdrop: #3b3b3b;
    --card: #050505;
    --gold: #b89a74;
    --white: #ffffff;
    --rule: #6a6a6a;
  }
  * { margin: 0; padding: 0; box-sizing: border-box; }
  html, body { width: 1200px; height: 689px; overflow: hidden; }
  body {
    background: var(--backdrop);
    font-family: "Arimo", Arial, sans-serif;
    position: relative;
  }
  .card {
    position: absolute;
    top: 196px;
    width: 520px;
    height: 297px;
    background: var(--card);
    border-radius: 18px;
    overflow: hidden;
  }
  .card-front { left: 50px; }
  .card-back { left: 630px; }

  .brand {
    display: flex;
    align-items: center;
    gap: 10px;
  }
  .brand-dot {
    width: 14px; height: 14px;
    border-radius: 50%;
    background: var(--gold);
    flex-shrink: 0;
  }
  .brand-name {
    color: var(--white);
    font-weight: 700;
    text-transform: uppercase;
    letter-spacing: 1px;
    line-height: 1.05;
  }
  .card-front .brand {
    position: absolute;
    left: 50%; top: 50%;
    transform: translate(-50%, -50%);
  }
  .card-front .brand-name { font-size: 26px; }
  .card-back .brand {
    position: absolute;
    right: 36px; top: 44px;
  }
  .card-back .brand-name { font-size: 19px; }

  .divider {
    position: absolute;
    left: 30px; right: 30px; top: 158px;
    height: 1px;
    background: var(--rule);
  }
  .holder {
    position: absolute;
    left: 30px; top: 108px;
  }
  .holder-name {
    color: var(--gold);
    font-weight: 700;
    font-size: 24px;
  }
  .holder-title {
    color: #bdbdbd;
    font-size: 14px;
    margin-top: 2px;
  }
  .contacts {
    position: absolute;
    left: 30px; top: 170px;
    list-style: none;
  }
  .contacts li {
    display: flex;
    align-items: center;
    gap: 10px;
    color: var(--white);
    font-size: 15px;
    line-height: 20px;
  }
  .contacts svg { width: 12px; height: 12px; flex-shrink: 0; }
  .address {
    position: absolute;
    right: 30px; top: 170px;
    text-align: right;
    color: var(--white);
    font-size: 15px;
    line-height: 20px;
    font-style: normal;
  }
  .edge-band {
    position: absolute;
    left: 0; right: 0; bottom: 0;
    height: 14px;
  }
  .edge-band .gold {
    position: absolute;
    left: 0; bottom: 0;
    width: 74%; height: 6px;
    background: var(--gold);
  }
  .edge-band .light {
    position: absolute;
    right: 0; bottom: 0;
    width: 26%; height: 14px;
    background: var(--white);
  }
</style>
</head>
<body>
  <section class="card card-front">
    <div class="brand">
      <span class="brand-dot"></span>
      <span class="brand-name">Birch Flooring Supply</span>
    </div>
  </section>

  <section class="card card-back">
    <div class="brand">
      <span class="brand-dot"></span>
      <span class="brand-name">Birch Flooring Supply</span>
    </div>

    <div class="holder">
      <div class="holder-name">Daniel Reed</div>
      <div class="holder-title">President</div>
    </div>

    <div class="divider"></div>

    <ul class="contacts">
      <li>
        <svg viewBox="0 0 12 12"><path d="M2.5 1 L4.5 1 L5.3 3.6 L4 4.6 Q5 7 7.4 8 L8.4 6.7 L11 7.5 L11 9.5 Q10 11 8.5 11 Q1 9 1 3.5 Q1 2 2.5 1 Z" fill="var(--white)"/></svg>
        555-214-0187
      </li>
      <li>
        <svg viewBox="0 0 12 12"><rect x="3" y="0.7" width="6" height="10.6" rx="1" fill="none" stroke="var(--white)" stroke-width="1.2"/><circle cx="6" cy="9.5" r="0.7" fill="var(--white)"/></svg>
        555-306-4921
      </li>
      <li>
        <svg viewBox="0 0 12 12"><rect x="0.7" y="2.5" width="10.6" height="7.5" fill="none" stroke="var(--white)" stroke-width="1.2"/><path d="M0.7 2.5 L6 6.8 L11.3 2.5" fill="none" stroke="var(--white)" stroke-width="1.2"/></svg>
        info@birchflooringsupply.com
      </li>
    </ul>

    <address class="address">
      412 Cedar Row<br>
      Halton, Canada 20418<br>
      www.birchflooringsupply.com
    </address>

    <div class="edge-band">
      <span class="gold"></span>
      <span class="light"></span>
    </div>
  </section>
</body>
</html>
```